Gin Bottle label design

A label for three Gins, 1 Apple flavoured, 1 Bilberry flavoured and one London Dry Gin. All need to incorporate the business logo that i've attached along with the bottle we intend to use. The gin is 40% and will be in a 70cl bottle

```html
<!DOCTYPE html>
<html lang="en">
<head>
<meta charset="UTF-8">
<title>Harlow Gin Labels</title>
<link href="https://fonts.googleapis.com/css2?family=Cormorant+SC:wght@500;700&family=Playfair+Display:wght@400&display=swap" rel="stylesheet">
<style>
  :root {
    --canvas: #ebebeb;
    --cream: #f5f0dd;
    --botanical-light: #ece7d0;
    --botanical-dark: #c9c6ac;
    --scene-light: #efe9d6;
    --scene-dark: #cfc8b2;
    --berry-light: #eee8d5;
    --berry-dark: #c6c3b4;
    --maroon: #7a1434;
    --ink-light: #fbf6ea;
  }
  * { margin: 0; padding: 0; box-sizing: border-box; }
  html, body {
    width: 800px; height: 1200px; overflow: hidden;
    background: var(--canvas);
  }
  .sheet {
    width: 800px; height: 1200px;
    display: flex; flex-direction: column; align-items: center;
    justify-content: center; gap: 30px;
  }
  .label {
    position: relative;
    width: 500px; height: 360px;
    background: var(--cream);
    overflow: hidden;
    box-shadow: 0 1px 3px rgba(0,0,0,0.12);
  }
  .label-art {
    position: absolute; inset: 0;
  }
  .art-botanical {
    background: radial-gradient(circle at 30% 40%, var(--botanical-dark), var(--botanical-light) 70%);
  }
  .art-cityscape {
    background: linear-gradient(180deg, var(--scene-light) 0%, var(--scene-light) 35%, var(--scene-dark) 100%);
  }
  .art-berries {
    background: radial-gradient(circle at 75% 30%, var(--berry-dark), var(--berry-light) 65%);
  }
  .badge {
    position: absolute;
    left: 50%; top: 50%;
    width: 226px; height: 260px;
    transform: translate(-50%, -50%);
  }
  .badge svg { position: absolute; inset: 0; }
  .badge-text {
    position: absolute; inset: 0;
    display: flex; flex-direction: column; align-items: center;
    color: var(--ink-light);
    text-align: center;
  }
  .brand {
    margin-top: 52px;
    font-family: "Cormorant SC", serif;
    font-weight: 700;
    font-size: 17px;
    letter-spacing: 3px;
    padding-bottom: 3px;
    border-bottom: 1px solid var(--ink-light);
  }
  .variety {
    margin-top: 14px;
    font-family: "Cormorant SC", serif;
    font-weight: 500;
    font-size: 17px;
    letter-spacing: 0.5px;
  }
  .spirit {
    font-family: "Playfair Display", serif;
    font-weight: 400;
    font-size: 66px;
    line-height: 1;
    letter-spacing: 2px;
  }
  .abv {
    margin-top: 4px;
    font-family: "Cormorant SC", serif;
    font-weight: 500;
    font-size: 11px;
  }
  .volume {
    margin-top: 8px;
    font-family: "Cormorant SC", serif;
    font-weight: 700;
    font-size: 18px;
  }
</style>
</head>
<body>
<main class="sheet">

  <section class="label label-london-dry-botanical">
    <div class="label-art art-botanical" role="img" aria-label="Engraved botanical pattern of juniper leaves and branches in sage and cream"></div>
    <div class="badge">
      <svg viewBox="0 0 226 260" aria-hidden="true">
        <polygon points="113,0 226,65 226,195 113,260 0,195 0,65" fill="var(--maroon)"/>
        <polygon points="113,9 218,70 218,190 113,251 8,190 8,70" fill="none" stroke="var(--ink-light)" stroke-width="1"/>
      </svg>
      <div class="badge-text">
        <span class="brand">HARLOW</span>
        <span class="variety">London Dry</span>
        <span class="spirit">GIN</span>
        <span class="abv">40%</span>
        <span class="volume">70CL</span>
      </div>
    </div>
  </section>

  <section class="label label-london-dry-city">
    <div class="label-art art-cityscape" role="img" aria-label="Engraved London skyline with an observation wheel and river buildings in muted sepia tones"></div>
    <div class="badge">
      <svg viewBox="0 0 226 260" aria-hidden="true">
        <polygon points="113,0 226,65 226,195 113,260 0,195 0,65" fill="var(--maroon)"/>
        <polygon points="113,9 218,70 218,190 113,251 8,190 8,70" fill="none" stroke="var(--ink-light)" stroke-width="1"/>
      </svg>
      <div class="badge-text">
        <span class="brand">HARLOW</span>
        <span class="variety">London Dry</span>
        <span class="spirit">GIN</span>
        <span class="abv">40%</span>
        <span class="volume">70CL</span>
      </div>
    </div>
  </section>

  <section class="label label-bilberry">
    <div class="label-art art-berries" role="img" aria-label="Engraved bilberry branches with leaves, berries and flowers in grey and cream"></div>
    <div class="badge">
      <svg viewBox="0 0 226 260" aria-hidden="true">
        <polygon points="113,0 226,65 226,195 113,260 0,195 0,65" fill="var(--maroon)"/>
        <polygon points="113,9 218,70 218,190 113,251 8,190 8,70" fill="none" stroke="var(--ink-light)" stroke-width="1"/>
      </svg>
      <div class="badge-text">
        <span class="brand">HARLOW</span>
        <span class="variety">Bilberry Flavoured</span>
        <span class="spirit">GIN</span>
        <span class="abv">40%</span>
        <span class="volume">70CL</span>
      </div>
    </div>
  </section>

</main>
</body>
</html>
```